New locally owned rental company needs a flyer to circulate

Need flyer with logo, phone# and address. We rent cars to anyone with driver's license and proper insurance. Rates as low as $50/day. Can offer compact cars, mid-size and full size sedans. Also SUV's.

```html
<!DOCTYPE html>
<html lang="en">
<head>
<meta charset="utf-8">
<title>DriveLocal Rent a Car Flyer</title>
<link rel="stylesheet" href="https://fonts.googleapis.com/css2?family=Montserrat:wght@600;800;900&family=Open+Sans:wght@400;600;700&display=swap">
<style>
  :root {
    --green: #2bb24c;
    --green-dark: #1f8f3b;
    --blue: #1f4e9e;
    --blue-dark: #163a78;
    --white: #ffffff;
    --ink: #1d2a44;
    --photo-light: #e6e9ee;
    --photo-mid: #b8c0cc;
  }
  * { margin: 0; padding: 0; box-sizing: border-box; }
  html, body { width: 719px; height: 1200px; overflow: hidden; background: var(--white); }
  .flyer { position: relative; width: 719px; height: 1200px; overflow: hidden; font-family: "Open Sans", sans-serif; background: var(--white); }
  .backdrop { position: absolute; inset: 0; }
  .headline { position: absolute; left: 44px; top: 58px; font-family: "Montserrat", sans-serif; font-weight: 900; line-height: 0.95; font-size: 92px; letter-spacing: -1px; }
  .headline .rent { color: var(--green); display: block; }
  .headline .a-car { color: var(--blue); display: block; }
  .price-pin { position: absolute; left: 380px; top: 46px; width: 120px; height: 150px; }
  .price-pin .label { position: absolute; left: 0; top: 22px; width: 120px; text-align: center; color: var(--white); font-family: "Montserrat", sans-serif; }
  .price-pin .amount { font-size: 34px; font-weight: 800; display: block; line-height: 1; }
  .price-pin .unit { font-size: 14px; font-weight: 700; letter-spacing: 1px; }
  .rates { position: absolute; left: 505px; top: 178px; transform: rotate(-30deg); transform-origin: left top; color: var(--white); font-family: "Montserrat", sans-serif; font-weight: 800; font-size: 22px; line-height: 1.15; letter-spacing: 1px; white-space: nowrap; }
  .rates span { display: block; }
  .car-photo { position: absolute; left: 40px; top: 320px; width: 640px; height: 300px; border-radius: 8px; background: radial-gradient(ellipse at 50% 55%, var(--photo-light) 0%, var(--photo-mid) 70%, transparent 72%); }
  .info { position: absolute; top: 720px; left: 0; width: 719px; color: var(--white); }
  .col { position: absolute; top: 0; }
  .col-offers { left: 40px; width: 250px; }
  .col-rent { left: 300px; width: 340px; }
  .col h2 { font-family: "Montserrat", sans-serif; font-weight: 900; font-size: 40px; line-height: 1; text-transform: uppercase; }
  .col h2 .accent { color: var(--green); display: block; }
  .col ul { list-style: none; margin-top: 16px; }
  .col li { font-size: 17px; font-weight: 600; line-height: 1.55; text-transform: uppercase; }
  .col p { margin-top: 16px; font-size: 17px; font-weight: 600; line-height: 1.45; text-transform: uppercase; }
  .thumbs { position: absolute; top: 930px; left: 40px; width: 640px; display: flex; gap: 12px; }
  .thumb { flex: 1; height: 110px; border: 4px solid var(--white); background: linear-gradient(160deg, #c9d1dc, #6f7f96); }
  .footer { position: absolute; left: 0; top: 1065px; width: 719px; height: 135px; }
  .brand { position: absolute; left: 44px; top: 22px; color: var(--blue); font-family: "Montserrat", sans-serif; font-weight: 900; }
  .brand .name { font-size: 46px; line-height: 1; display: flex; align-items: center; gap: 10px; }
  .brand .dot { width: 18px; height: 18px; background: var(--green); border-radius: 50%; }
  .brand .tagline { font-size: 19px; font-weight: 800; margin-top: 6px; }
  .contact { position: absolute; left: 420px; top: 24px; color: var(--ink); }
  .phone { display: flex; align-items: center; gap: 10px; font-family: "Montserrat", sans-serif; font-weight: 800; font-size: 32px; color: var(--ink); }
  .address { margin-top: 8px; margin-left: 46px; font-size: 14px; line-height: 1.4; color: #4a5568; }
</style>
</head>
<body>
<main class="flyer">
  <svg class="backdrop" width="719" height="1200" viewBox="0 0 719 1200" aria-hidden="true">
    <polygon points="330,0 719,0 719,470" fill="var(--green)"/>
    <polygon points="719,470 719,520 560,300 600,300" fill="var(--blue)"/>
    <polygon points="0,690 719,600 719,1060 0,1060" fill="var(--blue)"/>
    <polygon points="0,660 300,640 0,700" fill="var(--green)"/>
    <polygon points="719,1040 719,1060 450,1060" fill="var(--green)"/>
  </svg>

  <h1 class="headline"><span class="rent">RENT</span><span class="a-car">A CAR</span></h1>

  <div class="price-pin">
    <svg width="120" height="150" viewBox="0 0 120 150" aria-hidden="true">
      <path d="M60 4 C28 4 4 28 4 60 C4 96 60 146 60 146 C60 146 116 96 116 60 C116 28 92 4 60 4 Z" fill="var(--blue)" stroke="var(--white)" stroke-width="4"/>
    </svg>
    <div class="label"><span class="amount">$50</span><span class="unit">PER DAY</span></div>
  </div>

  <div class="rates"><span>RATES AS LOW</span><span>AS $50/DAY</span></div>

  <div class="car-photo" role="img" aria-label="Photo of a silver mid-size sedan"></div>

  <section class="info">
    <div class="col col-offers">
      <h2>Our <span class="accent">Offers</span></h2>
      <ul>
        <li>Compact Cars</li>
        <li>Mid-Size</li>
        <li>Full Size Sedans</li>
        <li>SUV's</li>
      </ul>
    </div>
    <div class="col col-rent">
      <h2>Who Can <span class="accent">Rent</span></h2>
      <p>We rent cars to anyone with driver's license and proper insurance.</p>
    </div>
  </section>

  <div class="thumbs">
    <div class="thumb" role="img" aria-label="Photo of a blue compact car"></div>
    <div class="thumb" role="img" aria-label="Photo of a silver SUV"></div>
    <div class="thumb" role="img" aria-label="Photo of a red sedan"></div>
    <div class="thumb" role="img" aria-label="Photo of a white full size sedan"></div>
  </div>

  <footer class="footer">
    <div class="brand">
      <div class="name"><span class="dot"></span>DriveLocal</div>
      <div class="tagline">Car &amp; Van Rental</div>
    </div>
    <div class="contact">
      <div class="phone">
        <svg width="36" height="36" viewBox="0 0 36 36" aria-hidden="true">
          <circle cx="18" cy="18" r="18" fill="var(--green)"/>
          <path d="M12 9 l4 0 l2 5 l-3 2 c1 3 3 5 6 6 l2 -3 l5 2 l0 4 c0 1 -1 2 -2 2 c-9 0 -16 -7 -16 -16 c0 -1 1 -2 2 -2 z" fill="var(--white)"/>
        </svg>
        555-014-2290
      </div>
      <div class="address">4820 Oak Ridge Parkway<br>Millbrook, AL 35000</div>
    </div>
  </footer>
</main>
</body>
</html>
```